Company or website name
- The Quillstone Movers and Storage
- Links to the website
- Quillstonehauling.com
- Describe your company and organization and target audience
- Residential and commercial moving and relocation service that needs a website redesign.
- The design should have the following
- I NEED THE WEBSITE TO BE SIMPLE AND STRAIGHT TO THE POINT...MAIN CONCERN IS THAT THEY FILL OUT INFORMATION TO GET QUOTE. SITE EXAMPLE THAT I LIKE IS ( WWW.MYPELDRAN.COM) https://www.orvikhaulage.com/

```html
<!DOCTYPE html>
<html lang="en">
<head>
<meta charset="utf-8">
<title>Quillstone Movers and Storage</title>
<link rel="stylesheet" href="https://fonts.googleapis.com/css2?family=Montserrat:wght@400;500;600;700&display=swap">
<style>
:root{
  --red:#f50000;
  --ink:#111111;
  --muted:#8a8a8a;
  --soft:#f2f2f2;
  --field:#ececec;
  --white:#ffffff;
  --star:#f5b400;
}
*{box-sizing:border-box;margin:0;padding:0}
html,body{width:1200px;height:3787px;overflow:hidden}
body{font-family:'Montserrat',sans-serif;color:var(--ink);background:var(--white);position:relative}
.abs{position:absolute}
.center{left:0;width:1200px;text-align:center}

/* header */
.site-header{top:0;left:0;width:1200px;height:98px;background:var(--white)}
.brand{display:flex;align-items:center;gap:10px;font-weight:700;letter-spacing:3px;color:var(--ink)}
.brand-dot{width:30px;height:30px;background:var(--ink);border-radius:50%}
.header-brand{left:88px;top:30px;font-size:30px}
.nav a{position:absolute;top:40px;font-size:15px;font-weight:500;color:var(--ink);text-decoration:none}
.btn-quote-top{left:963px;top:29px;width:150px;height:39px;background:var(--red);color:var(--white);border-radius:4px;font-size:13px;font-weight:700;display:flex;align-items:center;justify-content:center}

/* hero */
.hero{top:98px;left:0;width:1200px;height:617px;background:linear-gradient(180deg,#6f7d8f 0%,#9aa3ad 35%,#5b6a4d 75%,#3f4a38 100%)}
.hero-title{top:262px;font-size:47px;font-weight:700;color:var(--white)}
.hero-sub{top:324px;font-size:15px;font-weight:500;color:var(--white)}
.section-gray{top:715px;left:0;width:1200px;height:911px;background:var(--soft)}

/* quote card */
.quote-card{left:203px;top:407px;width:794px;height:552px;background:var(--white);border-radius:8px;box-shadow:0 2px 8px rgba(0,0,0,.12)}
.quote-title{top:34px;left:0;width:794px;text-align:center;font-size:19px;font-weight:700}
.tab{top:74px;width:94px;height:92px;border-radius:4px;background:var(--soft);color:#777;font-size:11px;display:flex;flex-direction:column;align-items:center;justify-content:center;gap:8px}
.tab.active{background:var(--red);color:var(--white);font-weight:600}
.field-label{font-size:14px;font-weight:500}
.field{width:230px;height:38px;background:var(--field);font-size:14px;color:#b5b5b5;padding:0 11px;display:flex;align-items:center}
.btn{height:49px;width:174px;display:flex;align-items:center;justify-content:center;font-size:16px;font-weight:600;border-radius:2px}
.btn-red{background:var(--red);color:var(--white)}
.btn-outline{border:1.5px solid #999;color:var(--ink);background:var(--white)}

/* services */
.section-title{font-size:38px;font-weight:700}
.service-card{top:1129px;width:231px;height:400px;background:var(--white);box-shadow:0 1px 6px rgba(0,0,0,.15);text-align:center}
.service-card.featured{background:var(--red);color:var(--white)}
.service-icon{position:absolute;left:65px;top:46px}
.service-name{position:absolute;top:164px;left:0;width:100%;font-size:28px;font-weight:700}
.service-text{position:absolute;top:216px;left:20px;width:191px;font-size:15.5px;line-height:22px;color:var(--muted)}
.featured .service-text{color:var(--white)}
.service-link{position:absolute;top:360px;left:0;width:100%;font-size:14.5px;font-weight:600;color:var(--red)}
.featured .service-link{color:var(--white)}

/* about */
.about-photo{left:88px;top:1893px;width:510px;height:394px;background:linear-gradient(180deg,#4f6a3a 0%,#c9ccce 35%,#d7d9db 60%,#5f8a3a 82%,#4d7a2f 100%)}
.about-title{left:663px;top:1933px;font-size:38px;font-weight:700}
.about-text{left:663px;top:1992px;width:420px;font-size:15.5px;line-height:22px;color:#333}
.btn-small{left:663px;top:2162px;width:150px;height:38px;background:var(--red);color:var(--white);font-size:16px;font-weight:600;border-radius:3px;display:flex;align-items:center;justify-content:center}

/* testimonials */
.section-gray-2{top:2423px;left:0;width:1200px;height:864px;background:var(--soft)}
.review{width:455px}
.review p{font-size:15.5px;line-height:22px;color:#333}
.reviewer{display:flex;align-items:center;gap:17px;margin-top:24px}
.avatar{width:59px;height:59px;border-radius:50%;background:#6b5a4c}
.reviewer-name{font-size:16px;font-weight:600}
.stars{color:var(--star);font-size:15px;letter-spacing:2px}
.arrow{top:2680px}

/* cta */
.cta{left:88px;top:2944px;width:1025px;height:238px;background:var(--red);border-radius:8px;color:var(--white);text-align:center}
.cta h2{position:absolute;top:40px;left:0;width:100%;font-size:40px;font-weight:600}
.cta p{position:absolute;top:94px;left:0;width:100%;font-size:15px;font-weight:500;line-height:22px}
.cta-btn{position:absolute;left:419px;top:153px;width:186px;height:46px;background:var(--ink);color:var(--white);font-size:16px;font-weight:600;border-radius:3px;display:flex;align-items:center;justify-content:center}

/* footer */
.footer-brand{left:129px;top:3412px;font-size:40px}
.footer-brand .brand-dot{width:40px;height:40px}
.footer-text{left:117px;top:3484px;width:300px;font-size:13.5px;line-height:25px;color:#555}
.social{top:3586px;width:23px;height:23px;border-radius:50%;background:var(--ink)}
.footer-col h4{font-size:18px;font-weight:600;margin-bottom:18px}
.footer-col a{display:block;font-size:15px;color:#666;text-decoration:none;margin-bottom:16px;height:22px}
.footer-rule{top:3728px;left:0;width:1200px;height:1px;background:#bbb}
.copyright{top:3750px;font-size:12px;color:#666}
</style>
</head>
<body>

<header class="site-header abs">
  <div class="brand header-brand abs"><span class="brand-dot"></span>QUILLSTONE</div>
  <nav class="nav">
    <a style="left:378px">About</a>
    <a style="left:475px">Moving Services &#8964;</a>
    <a style="left:669px">Resources &#8964;</a>
    <a style="left:816px">Contacts</a>
  </nav>
  <div class="btn-quote-top abs">Request a Quote</div>
</header>

<section class="hero abs" role="img" aria-label="Photo of a white moving truck parked on a suburban street"></section>
<h1 class="hero-title abs center">We Help Move Lives Forward</h1>
<p class="hero-sub abs center">Providing Local, Long Distance Residential and Commercial Moving Services Since 2006</p>

<div class="section-gray abs"></div>

<form class="quote-card abs">
  <h2 class="quote-title abs">GET A FREE MOVING QUOTE!</h2>
  <div class="tab active abs" style="left:188px">
    <svg width="40" height="38" viewBox="0 0 40 38"><path d="M4 18 L20 4 L36 18 V36 H4 Z" fill="#fff"/><rect x="14" y="24" width="12" height="12" fill="#f50000"/></svg>Residential</div>
  <div class="tab abs" style="left:296px">
    <svg width="40" height="38" viewBox="0 0 40 38"><path d="M4 14 Q20 0 36 14 V36 H4 Z" fill="#888"/><rect x="9" y="20" width="9" height="16" fill="#f2f2f2"/><rect x="22" y="20" width="9" height="16" fill="#f2f2f2"/></svg>Senior</div>
  <div class="tab abs" style="left:403px">
    <svg width="40" height="38" viewBox="0 0 40 38"><rect x="4" y="2" width="32" height="6" fill="#888"/><rect x="7" y="10" width="26" height="10" fill="#888"/><rect x="4" y="22" width="32" height="14" fill="#888"/><rect x="15" y="26" width="10" height="10" fill="#f2f2f2"/></svg>Commercial</div>
  <div class="tab abs" style="left:512px">
    <svg width="40" height="38" viewBox="0 0 40 38"><path d="M4 10 L20 2 L36 10 V36 H4 Z" fill="#888"/><rect x="10" y="16" width="20" height="3" fill="#f2f2f2"/><rect x="10" y="22" width="20" height="3" fill="#f2f2f2"/><rect x="10" y="28" width="20" height="3" fill="#f2f2f2"/></svg>Storage</div>

  <label class="field-label abs" style="left:151px;top:202px">I am moving from . . .</label>
  <div class="field abs" style="left:151px;top:228px">Zip Code</div>
  <label class="field-label abs" style="left:413px;top:202px">I am moving to . . .</label>
  <div class="field abs" style="left:413px;top:228px">Zip Code</div>
  <label class="field-label abs" style="left:151px;top:281px">Moving Date</label>
  <div class="field abs" style="left:151px;top:307px">02 / 31 / 2022</div>
  <label class="field-label abs" style="left:413px;top:281px">Full Name</label>
  <div class="field abs" style="left:413px;top:307px">Alex Rivera</div>
  <label class="field-label abs" style="left:151px;top:360px">E-Mail Address</label>
  <div class="field abs" style="left:151px;top:386px">email@mail.com</div>
  <label class="field-label abs" style="left:413px;top:360px">Phone Number</label>
  <div class="field abs" style="left:413px;top:386px">(+000) 000 0000</div>

  <div class="btn btn-red abs" style="left:207px;top:450px">Free Quote</div>
  <div class="btn btn-outline abs" style="left:412px;top:450px">Contact Us</div>
</form>

<h2 class="section-title abs center" style="top:1044px">Moving Services</h2>

<article class="service-card featured abs" style="left:88px">
  <svg class="service-icon" width="100" height="98" viewBox="0 0 100 98"><circle cx="84" cy="12" r="10" fill="#fff"/><path d="M6 50 L50 14 L94 50 V96 H6 Z" fill="#fff"/><rect x="40" y="62" width="22" height="34" fill="#f50000"/></svg>
  <h3 class="service-name">Residential</h3>
  <p class="service-text">We are the residential movers who strive to make your relocation experience simplified - regardless of whether you are moving...</p>
  <span class="service-link">Learn More</span>
</article>
<article class="service-card abs" style="left:350px">
  <svg class="service-icon" width="100" height="98" viewBox="0 0 100 98"><rect x="4" y="2" width="92" height="12" fill="#f50000"/><rect x="10" y="20" width="80" height="26" fill="#f50000"/><rect x="4" y="52" width="92" height="44" fill="#f50000"/><rect x="38" y="62" width="24" height="34" fill="#fff"/></svg>
  <h3 class="service-name">Commercial</h3>
  <p class="service-text">As commercial movers, Quillstone Inc is one of the industry leaders in providing the highest quality services at competitive</p>
  <span class="service-link">Learn More</span>
</article>
<article class="service-card abs" style="left:617px">
  <svg class="service-icon" width="100" height="98" viewBox="0 0 100 98"><path d="M2 30 Q50 -10 98 30 V96 H2 Z" fill="#f50000"/><rect x="14" y="50" width="30" height="46" fill="#fff"/><rect x="56" y="50" width="30" height="46" fill="#fff"/></svg>
  <h3 class="service-name">Senior</h3>
  <p class="service-text">s the thought of moving as a senior too daunting for you? It can often times be a draining process. If you are concerned about...</p>
  <span class="service-link">Learn More</span>
</article>
<article class="service-card abs" style="left:882px">
  <svg class="service-icon" width="100" height="98" viewBox="0 0 100 98"><path d="M2 22 L50 0 L98 22 V96 H2 Z" fill="#f50000"/><rect x="16" y="36" width="68" height="8" fill="#fff"/><rect x="16" y="52" width="68" height="8" fill="#fff"/><rect x="16" y="68" width="68" height="28" fill="#fff"/><rect x="46" y="68" width="8" height="28" fill="#f50000"/></svg>
  <h3 class="service-name">Storage</h3>
  <p class="service-text">Need to move your extra belongings into a storage facility? If you want a company to handle all your storage needs from A to Z..</p>
  <span class="service-link">Learn More</span>
</article>

<h2 class="section-title abs center" style="top:1717px">Moving Families &amp; Businesses For Over A Decade</h2>
<p class="abs center" style="top:1778px;font-size:20px;line-height:30px">As movers since 2007, Quillstone Inc has an expertise in transportation and storage services<br>that is unequaled by other moving companies.</p>

<div class="about-photo abs" role="img" aria-label="Photo of a white company box truck parked on a lawn beside a house"></div>
<h2 class="about-title abs">About Us</h2>
<p class="about-text abs">At Quillstone Inc we coordinate local, long distance moves that incorporate all the necessary moving services to est serve your individual move. In addition, we offer our commercial clients a wide array of specialized transportation services for high-value products. We are committed to safe, simple moving experiences for family, businesses and employees.</p>
<div class="btn-small abs">Learn More</div>

<div class="section-gray-2 abs"></div>
<h2 class="section-title abs center" style="top:2511px">What clients are saying</h2>

<svg class="arrow abs" style="left:46px" width="20" height="40" viewBox="0 0 20 40"><path d="M16 4 L4 20 L16 36" fill="none" stroke="#aaa" stroke-width="4"/></svg>
<svg class="arrow abs" style="left:1130px" width="20" height="40" viewBox="0 0 20 40"><path d="M4 4 L16 20 L4 36" fill="none" stroke="#aaa" stroke-width="4"/></svg>

<div class="review abs" style="left:119px;top:2633px">
  <p>Great Service...Easy...Stress free move. Provided accurate move estimate. Professional staff all around. From Estimate to delivery. Professional and Friendly pick-up, Transportation, and Delivery. Thank You so Much.</p>
  <div class="reviewer"><div class="avatar" role="img" aria-label="Client portrait"></div><div><div class="reviewer-name">Marcus, Rivergate TX</div><div class="stars">★★★★★</div></div></div>
</div>
<div class="review abs" style="left:625px;top:2633px">
  <p>Both the folks that packed up my belongings and the folks that delivered them were very efficient and professional. I was a little anxious about my antique furniture, but everything arrived in great shape.</p>
  <div class="reviewer"><div class="avatar" style="background:#5d6a78" role="img" aria-label="Client portrait"></div><div><div class="reviewer-name">Dana L., Harbor Bay FL</div><div class="stars">★★★★★</div></div></div>
</div>

<section class="cta abs">
  <h2>Let's Get You A Free Quote</h2>
  <p>No matter the size or scope of your relocation, Quillstone Moving can offer<br>you the simple and stress-free services you are looking for.</p>
  <div class="cta-btn">Free Quote Now</div>
</section>

<footer>
  <div class="brand footer-brand abs"><span class="brand-dot"></span>QUILLSTONE</div>
  <p class="footer-text abs">Lorem ipsum, or lipsum as it is sometimes known, is dummy text used in laying out print, graphic or web designs. .</p>
  <span class="social abs" style="left:160px" aria-label="Social link"></span>
  <span class="social abs" style="left:207px" aria-label="Social link"></span>
  <span class="social abs" style="left:253px" aria-label="Social link"></span>
  <span class="social abs" style="left:298px" aria-label="Social link"></span>

  <div class="footer-col abs" style="left:504px;top:3438px"><h4>Quick Links</h4><a>About</a><a>Moving Services</a><a>Resources</a><a>Contacts</a></div>
  <div class="footer-col abs" style="left:725px;top:3438px"><h4>User Links</h4><a>Account</a><a>Get Quote</a><a>Message</a><a>Logout</a></div>
  <div class="footer-col abs" style="left:913px;top:3438px"><h4>Information</h4><a>Privacy Policy</a><a>Terms &amp; Conditions</a></div>

  <div class="footer-rule abs"></div>
  <p class="copyright abs center">Copyright © 2022 by Quillstone. All rights reserved.</p>
</footer>

</body>
</html>
```